Diesel injection diagnostics and repairs

I am after a business card design for my business.
The business; repairs diesel fuel systems on 4wds, trucks, earthmoving equipment,can do mobile repairs and diagnostics
The business design can basic but effective, I guess some colours such as green and black or even blue......
The end result should reflect the business name and logo and what the business can do

Industry/Entity Type

Business

Contact Information for Business Card

BW Diesel Injection PTY LTD
bw_diesel@trovamail.net
Dennis Holt
0491570156

```html
<!DOCTYPE html>
<html lang="en">
<head>
<meta charset="utf-8">
<title>BW Diesel Injection – Business Card</title>
<link rel="stylesheet" href="https://fonts.googleapis.com/css2?family=Arimo:wght@400;700&display=swap">
<style>
  :root {
    --navy: #0f2f5f;
    --white: #ffffff;
    --ink: #111111;
    --paper: #f7f7f7;
    --faint: #e6e6e6;
    --backdrop: #d9d6d1;
  }
  * { margin: 0; padding: 0; box-sizing: border-box; }
  html, body {
    width: 1200px; height: 790px; overflow: hidden;
    background: var(--backdrop);
    font-family: "Arimo", Arial, sans-serif;
  }
  .card {
    position: absolute; top: 245px;
    width: 520px; height: 300px;
    overflow: hidden;
    box-shadow: 0 6px 18px rgba(0,0,0,.18);
  }
  .card--front { left: 50px; background: var(--navy); color: var(--white); }
  .card--back { left: 630px; background: var(--paper); color: var(--ink); }

  /* brand lockup */
  .brand { position: absolute; display: flex; align-items: flex-start; gap: 12px; font-weight: 700; }
  .brand__mark { width: 40px; height: 40px; flex: none; background: currentColor; }
  .brand__name { font-size: 32px; line-height: 1; letter-spacing: -0.3px; white-space: nowrap; }
  .brand__legal { display: flex; align-items: center; gap: 10px; font-size: 11px; margin-top: 4px; letter-spacing: .5px; }

  .card--front .brand { left: 30px; top: 38px; }
  .rule { position: absolute; height: 5px; background: var(--white); }
  .rule--upper { left: 82px; right: 22px; top: 94px; }
  .rule--lower { left: 30px; right: 22px; top: 108px; }

  .services { position: absolute; right: 22px; bottom: 26px; text-align: right; text-transform: uppercase; }
  .services__main { font-size: 16.5px; letter-spacing: .4px; }
  .services__more { font-size: 10.5px; margin-top: 5px; letter-spacing: .3px; }

  /* back */
  .decor-circle {
    position: absolute; right: -40px; top: 10px;
    width: 280px; height: 280px; border-radius: 50%;
    background: var(--faint);
  }
  .card--back .brand { left: 26px; top: 205px; color: var(--navy); }
  .card--back .brand__name { font-size: 26px; color: var(--ink); }
  .card--back .brand__legal { color: var(--ink); }
  .card--back .brand__mark { width: 34px; height: 34px; }
  .brand__rule { display: block; width: 150px; height: 4px; background: var(--navy); }

  .contact { position: absolute; right: 24px; top: 56px; text-align: right; }
  .contact__name { font-size: 22px; font-weight: 700; text-transform: uppercase; letter-spacing: .3px; margin-bottom: 8px; }
  .contact__line { display: flex; justify-content: flex-end; align-items: center; gap: 8px; font-size: 16px; margin-top: 5px; }
  .contact__icon { width: 13px; height: 13px; flex: none; }
</style>
</head>
<body>
  <section class="card card--front">
    <div class="brand">
      <span class="brand__mark"></span>
      <div class="brand__name">BW Diesel Injection<span class="brand__legal">PTY LTD</span></div>
    </div>
    <div class="rule rule--upper"></div>
    <div class="rule rule--lower"></div>
    <div class="services">
      <p class="services__main">Repairs diesel fuel systems on 4WDs, trucks</p>
      <p class="services__more">Earthmoving equipment, can do mobile repairs and diagnostics</p>
    </div>
  </section>

  <section class="card card--back">
    <div class="decor-circle" aria-hidden="true"></div>
    <div class="brand">
      <span class="brand__mark"></span>
      <div class="brand__name">BW Diesel Injection<span class="brand__legal">PTY LTD<span class="brand__rule"></span></span></div>
    </div>
    <div class="contact">
      <p class="contact__name">Dennis Holt</p>
      <p class="contact__line">049 157 0156
        <svg class="contact__icon" viewBox="0 0 13 13" aria-label="phone"><rect width="13" height="13" fill="#0f2f5f"/><path d="M3.5 2.5h2l.7 2-1.2.8a5 5 0 0 0 2.7 2.7l.8-1.2 2 .7v2c0 .6-.4 1-1 1A7.5 7.5 0 0 1 2.5 3.5c0-.6.4-1 1-1z" fill="#fff"/></svg>
      </p>
      <p class="contact__line">bw_diesel@trovamail.net
        <svg class="contact__icon" viewBox="0 0 13 13" aria-label="email"><rect width="13" height="13" fill="#0f2f5f"/><rect x="2.5" y="3.5" width="8" height="6" fill="none" stroke="#fff"/><path d="M2.5 3.5l4 3.2 4-3.2" fill="none" stroke="#fff"/></svg>
      </p>
    </div>
  </section>
</body>
</html>
```